Stationary and business card for veterinary hospital
Brinsley Animal Hospital
Bright & Fun-filled
Doctors Name
Dr
1234 Any Street, Suite 100
Anytown, ZZ 90210
info@brinsleyah.com
brinsleyanimalhospital.com
fun creative use of the logo

```html
<!DOCTYPE html>
<html lang="en">
<head>
<meta charset="utf-8">
<title>Brinsley Animal Hospital – Stationery</title>
<link href="https://fonts.googleapis.com/css2?family=Open+Sans:wght@400;700&display=swap" rel="stylesheet">
<style>
:root{
  --bg:#e8ecef;
  --paper:#ffffff;
  --blue:#1c7fb3;
  --blue-light:#6cc0e4;
  --navy:#0d3a56;
  --slate:#3a4750;
  --ink:#4a5560;
  --muted:#9aa6ae;
}
*{box-sizing:border-box;margin:0;padding:0}
html,body{width:1200px;height:248px;overflow:hidden}
body{background:var(--bg);font-family:"Open Sans",Arial,sans-serif;color:var(--ink);position:relative}
.item{position:absolute;background:var(--paper);box-shadow:0 1px 3px rgba(0,0,0,.18);overflow:hidden}
.wave{position:absolute;left:0;width:100%;display:block}
.brand{display:flex;align-items:center;gap:3px;font-weight:700;color:var(--blue);line-height:1.05}
.brand .dot{flex:none;border-radius:50%;background:currentColor}
.on-dark .brand{color:#fff}
.small{font-size:3.6px;line-height:1.5}

/* business cards */
.card{width:100px;height:58px}
.card.dark{background:var(--navy)}
.card.slate{background:var(--slate)}
.card .brand{font-size:7px}
.card .brand .dot{width:9px;height:9px}
.card .center{position:absolute;inset:0;display:flex;align-items:center;justify-content:center}
.card .details{position:absolute;left:8px;top:28px;color:#fff;font-size:3.8px;line-height:1.5}
.card .name{font-weight:700;font-size:4.6px}

/* letterheads */
.letter{width:140px;height:200px;top:22px}
.letter .brand{position:absolute;top:12px;left:0;right:0;justify-content:center;font-size:7px}
.letter .brand .dot{width:10px;height:10px}
.letter .body{position:absolute;left:14px;right:14px;top:46px}
.letter .body p{margin-bottom:4px}
.letter .footer{position:absolute;bottom:4px;left:0;right:0;text-align:center;color:#fff;font-size:3.4px}

/* compliment cards */
.slip{width:110px;height:46px}
.slip .brand{position:absolute;left:8px;top:8px;font-size:5.5px}
.slip .brand .dot{width:7px;height:7px}

/* envelopes */
.envelope{width:200px;height:50px}
.envelope.back{background:var(--blue)}
.envelope .brand{position:absolute;left:10px;top:8px;font-size:6px}
.envelope .brand .dot{width:8px;height:8px}
.envelope .addr{position:absolute;left:10px;top:22px;font-size:3.6px;color:var(--ink)}

/* folder */
.folder{left:940px;top:20px;width:236px;height:206px;background:var(--blue)}
.folder .brand{position:absolute;left:0;right:0;top:70px;justify-content:center;font-size:12px;color:#fff}
.folder .brand .dot{width:14px;height:14px}
.folder .flap-line{position:absolute;left:118px;top:0;bottom:0;border-left:1px solid rgba(255,255,255,.3)}
</style>
</head>
<body>

<!-- business cards -->
<div class="item card dark on-dark" style="left:16px;top:34px">
  <div class="center"><div class="brand"><span class="dot"></span>Brinsley Animal Hospital</div></div>
</div>
<div class="item card" style="left:124px;top:34px">
  <div class="center"><div class="brand"><span class="dot"></span>Brinsley Animal Hospital</div></div>
  <svg class="wave" style="bottom:0;height:12px" viewBox="0 0 100 20" preserveAspectRatio="none"><path d="M0 10 C30 0 60 18 100 6 V20 H0Z" fill="var(--blue)"/></svg>
</div>
<div class="item card slate on-dark" style="left:16px;top:104px">
  <div class="brand" style="position:absolute;left:8px;top:8px"><span class="dot"></span>Brinsley Animal Hospital</div>
  <div class="details"><div class="name">Dr. Jane Morrow</div>1234 Any Street, Suite 100<br>Anytown, ZZ 90210</div>
</div>
<div class="item card" style="left:124px;top:104px">
  <div class="brand" style="position:absolute;left:8px;top:8px"><span class="dot"></span>Brinsley Animal Hospital</div>
  <div class="details" style="color:var(--ink)"><div class="name" style="color:var(--blue)">Dr. Jane Morrow</div>info@brinsleyah.com<br>brinsleyanimalhospital.com</div>
  <svg class="wave" style="bottom:0;height:8px" viewBox="0 0 100 20" preserveAspectRatio="none"><path d="M0 10 C30 0 60 18 100 6 V20 H0Z" fill="var(--blue)"/></svg>
</div>
<div class="item card dark on-dark" style="left:16px;top:174px">
  <div class="center"><div class="brand"><span class="dot"></span>Brinsley Animal Hospital</div></div>
</div>
<div class="item card" style="left:124px;top:174px">
  <div class="details" style="color:var(--ink);top:18px"><div class="name" style="color:var(--blue)">(555) 010-0199</div>1234 Any Street, Suite 100<br>Anytown, ZZ 90210</div>
</div>

<!-- letterheads -->
<div class="item letter" style="left:256px">
  <div class="brand"><span class="dot"></span>Brinsley Animal Hospital</div>
  <div class="body small">
    <p>Dear Client,</p>
    <p>Thank you for trusting our team with the care of your pet. We look forward to seeing you again soon.</p>
    <p>Our doctors are here for wellness visits, dental care and surgery, with friendly staff ready every day of the week.</p>
    <p>Sincerely,<br>Dr. Jane Morrow</p>
  </div>
  <svg class="wave" style="bottom:0;height:22px" viewBox="0 0 100 20" preserveAspectRatio="none"><path d="M0 6 C30 -2 60 14 100 2 V20 H0Z" fill="var(--blue-light)"/><path d="M0 10 C30 2 60 18 100 6 V20 H0Z" fill="var(--blue)"/></svg>
  <div class="footer">1234 Any Street, Suite 100 · Anytown, ZZ 90210</div>
</div>
<div class="item letter" style="left:402px">
  <div class="brand"><span class="dot"></span>Brinsley Animal Hospital</div>
  <div class="body small">
    <p>Dear Client,</p>
    <p>Please find enclosed the records from your recent visit, along with care notes and reminders for upcoming vaccinations.</p>
    <p>Call us with any questions about your pet.</p>
    <p>Warm regards,<br>Dr. Jane Morrow</p>
  </div>
  <svg class="wave" style="bottom:0;height:22px" viewBox="0 0 100 20" preserveAspectRatio="none"><path d="M0 6 C30 -2 60 14 100 2 V20 H0Z" fill="var(--blue-light)"/><path d="M0 10 C30 2 60 18 100 6 V20 H0Z" fill="var(--blue)"/></svg>
  <div class="footer">info@brinsleyah.com · brinsleyanimalhospital.com</div>
</div>

<!-- compliment slips -->
<div class="item slip" style="left:564px;top:96px">
  <div class="brand"><span class="dot"></span>Brinsley Animal Hospital</div>
  <svg class="wave" style="bottom:0;height:10px" viewBox="0 0 100 20" preserveAspectRatio="none"><path d="M0 10 C30 0 60 18 100 6 V20 H0Z" fill="var(--blue)"/></svg>
</div>
<div class="item slip" style="left:564px;top:166px">
  <div class="brand"><span class="dot"></span>Brinsley Animal Hospital</div>
  <div class="small" style="position:absolute;left:8px;top:20px">With compliments from our team</div>
  <svg class="wave" style="bottom:0;height:10px" viewBox="0 0 100 20" preserveAspectRatio="none"><path d="M0 10 C30 0 60 18 100 6 V20 H0Z" fill="var(--blue)"/></svg>
</div>

<!-- envelopes -->
<div class="item envelope back on-dark" style="left:716px;top:90px">
  <svg class="wave" style="top:0;height:26px" viewBox="0 0 100 20" preserveAspectRatio="none"><path d="M0 0 L50 16 L100 0Z" fill="var(--navy)"/></svg>
</div>
<div class="item envelope" style="left:716px;top:150px">
  <div class="brand"><span class="dot"></span>Brinsley Animal Hospital</div>
  <div class="addr">1234 Any Street, Suite 100<br>Anytown, ZZ 90210</div>
  <svg class="wave" style="bottom:0;height:10px" viewBox="0 0 100 20" preserveAspectRatio="none"><path d="M0 10 C30 0 60 18 100 6 V20 H0Z" fill="var(--blue)"/></svg>
</div>

<!-- presentation folder -->
<div class="item folder">
  <div class="flap-line"></div>
  <div class="brand"><span class="dot"></span>Brinsley Animal Hospital</div>
  <svg class="wave" style="bottom:0;height:60px" viewBox="0 0 100 20" preserveAspectRatio="none"><path d="M0 8 C30 0 60 16 100 4 V20 H0Z" fill="var(--blue-light)"/><path d="M0 12 C30 4 60 20 100 8 V20 H0Z" fill="#ffffff"/></svg>
</div>

</body>
</html>
```